web design needed for jewellery inspired temporary tattoo company

Hi There

I need a web design for a new company I'm launching called coral glow luxe
Im a retailer of flash tattoos - temporary gold and silver metallic tattoos

These are the next new craze with many celebrities already displaying them whilst being lapped on their holidays

i need a very classy upmarket wow web design with an e commerce shop attached

I also offer marlow q bronze mist so will need a page to link to where people can get a tan and tattoo - so maybe as a box on the main page

As A guide I'm looking for someone to put their unique spin on an american website which is currently selling the same type of product
www.glintmarkz.com

the final design should oozzzz 'rich list ' coral luxe - think st tropez Monaco and needs to be linked to all my social media

please seepintrest flash tattoos for what we sell
I've attached my logo

I can't wait to hear from you all
many Thanks

Fiona Dembrey
www.coralglowluxe.co.uk

Target Market(s)

20 to 30's young party rich list glamous girls - festival boho cool beach LA

Industry/Entity Type

It Company

Number of Pages Required

3 page

Font styles to use
Script

Requirements
Must have
• a beach feel
• pictures of people wearing the tattoos
• an ecommerce site
• be easy to navigate
• my logo
• the wow factor
Nice to have
• a really classy expensive feel to the website
Should not have
• a cheap plain look

```html
<!DOCTYPE html>
<html lang="en">
<head>
<meta charset="utf-8">
<title>Coral Glow Luxe — Home</title>
<link rel="stylesheet" href="https://fonts.googleapis.com/css2?family=Open+Sans:wght@400;600;700&family=Raleway:wght@400;500;600;700&display=swap">
<style>
  :root {
    --header-bg: #232425;
    --nav-rule: #3a3b3c;
    --gold: #c9a24a;
    --gold-button: #d9a826;
    --text-light: #e6e6e6;
    --text-muted: #a9a9a9;
    --band-bg: #f0f0f0;
    --band-text: #555555;
    --ink: #222222;
    --ink-soft: #444444;
    --rule: #dcdcdc;
    --panel-dark: rgba(28, 28, 28, 0.86);
    --white: #ffffff;
  }
  * { box-sizing: border-box; margin: 0; padding: 0; }
  html, body { width: 1200px; height: 1183px; overflow: hidden; background: var(--white); }
  body { position: relative; font-family: "Open Sans", Arial, sans-serif; color: var(--ink); }

  /* Header */
  .site-header { position: absolute; left: 0; top: 0; width: 1200px; height: 192px; background: var(--header-bg); }
  .utility-left { position: absolute; left: 87px; top: 60px; display: flex; align-items: center; gap: 8px; font-size: 11px; color: var(--text-muted); }
  .flag-chip { width: 12px; height: 8px; background: #c8c8d8; display: inline-block; }
  .caret { width: 0; height: 0; border-left: 4px solid transparent; border-right: 4px solid transparent; border-top: 4px solid var(--text-muted); display: inline-block; margin-left: 3px; }
  .search { position: absolute; left: 87px; top: 90px; width: 195px; height: 22px; border-bottom: 1px solid #555; font-size: 12px; color: var(--text-muted); }
  .search svg { position: absolute; right: 4px; top: 2px; }
  .brand { position: absolute; left: 500px; top: 44px; width: 200px; text-align: center; }
  .brand-dot { width: 46px; height: 46px; border: 2px solid var(--gold); border-radius: 50%; margin: 0 auto 10px; }
  .brand-name { font-family: "Raleway", Arial, sans-serif; font-weight: 500; font-size: 17px; color: var(--gold); letter-spacing: 1px; }
  .utility-right { position: absolute; right: 101px; top: 61px; font-size: 11px; color: var(--text-muted); display: flex; align-items: center; gap: 6px; }
  .cart { position: absolute; right: 101px; top: 93px; font-size: 11px; color: var(--text-muted); display: flex; align-items: center; gap: 8px; }

  .main-nav { position: absolute; left: 0; top: 158px; width: 1200px; height: 34px; border-top: 1px solid var(--nav-rule); display: flex; justify-content: center; align-items: center; }
  .main-nav a { color: var(--white); text-decoration: none; font-size: 13px; font-weight: 700; letter-spacing: 0.4px; margin: 0 11px; }
  .main-nav .account-link { color: var(--text-muted); font-weight: 600; margin-left: 18px; }
  .main-nav .account-link b { color: var(--text-muted); font-weight: 600; }
  .main-nav .account-link span { font-weight: 400; }

  .shipping-band { position: absolute; left: 0; top: 192px; width: 1200px; height: 62px; background: var(--band-bg); display: flex; justify-content: center; align-items: center; font-size: 17px; color: var(--band-text); letter-spacing: 0.6px; }
  .shipping-band strong { font-weight: 700; margin-right: 6px; }
  .shipping-band u { margin-left: 6px; }

  /* Hero */
  .hero { position: absolute; left: 88px; top: 269px; width: 1012px; height: 417px; }
  .hero-photo { position: absolute; inset: 0; background: linear-gradient(180deg, #4d8fd2 0%, #9cc6ea 30%, #5fc9cf 44%, #3fb4b8 56%, #cfd9cf 66%, #e6d8bf 100%); }
  .hero-panel { position: absolute; left: 0; top: 0; width: 305px; height: 417px; background: var(--panel-dark); }
  .hero-copy { position: absolute; left: 87px; top: 84px; width: 182px; font-size: 12.5px; line-height: 16px; color: var(--white); }
  .hero-price { position: absolute; left: 88px; top: 163px; width: 188px; height: 52px; border-top: 1px solid #ddd; border-bottom: 1px solid #ddd; text-align: center; color: var(--white); font-size: 26px; line-height: 50px; }
  .hero-price strong { font-weight: 700; font-size: 31px; }
  .hero-kicker { position: absolute; left: 86px; top: 237px; font-size: 16px; font-weight: 700; color: var(--white); letter-spacing: 0.3px; }
  .hero-title { position: absolute; left: 86px; top: 262px; font-size: 35px; line-height: 42px; color: var(--white); font-weight: 400; }
  .hero-cta { position: absolute; left: 87px; top: 313px; width: 106px; height: 32px; background: var(--gold-button); color: var(--white); font-size: 15px; line-height: 32px; text-align: center; letter-spacing: 0.3px; }
  .hero-arrow { position: absolute; top: 180px; width: 40px; height: 40px; border-radius: 50%; background: rgba(40, 40, 40, 0.55); }
  .hero-arrow svg { position: absolute; left: 15px; top: 12px; }
  .hero-arrow.prev { left: 13px; }
  .hero-arrow.next { right: 15px; background: rgba(60, 60, 60, 0.45); }
  .hero-dots { position: absolute; right: 18px; bottom: 18px; display: flex; gap: 10px; }
  .hero-dots span { width: 12px; height: 12px; border: 1px solid #bbb; background: #e7e7e7; }
  .hero-dots .active { background: #111; border-color: #111; }

  /* Product tabs */
  .tabs { position: absolute; left: 370px; top: 728px; width: 421px; height: 40px; border-bottom: 1px solid var(--rule); font-family: "Raleway", Arial, sans-serif; font-size: 17px; color: var(--ink-soft); }
  .tab { position: absolute; top: 4px; }
  .tab.active { left: 38px; color: var(--ink); }
  .tab.latest { left: 193px; }
  .tab.special { left: 298px; }
  .tab-underline { position: absolute; left: 38px; top: 37px; width: 122px; height: 3px; background: #333; }
  .tab-pointer { position: absolute; left: 461px; top: 772px; }
  .carousel-nav { position: absolute; left: 1064px; top: 737px; display: flex; gap: 14px; }

  .products { position: absolute; left: 88px; top: 813px; width: 1012px; display: flex; gap: 17px; }
  .product { width: 240px; text-align: center; font-family: "Raleway", Arial, sans-serif; }
  .product-photo { position: relative; width: 240px; height: 301px; }
  .product-photo.skin-a { background: linear-gradient(160deg, #3a2e28 0%, #8a5a44 45%, #c99379 75%, #e6c2ac 100%); }
  .product-photo.skin-b { background: linear-gradient(150deg, #e9e4dc 0%, #7a5648 35%, #4a5a3a 70%, #c38a6e 100%); }
  .product-photo.skin-c { background: linear-gradient(180deg, #2fa79a 0%, #a36e4e 18%, #c88d69 60%, #d7b49a 100%); }
  .product-photo.skin-d { background: linear-gradient(135deg, #7b5a46 0%, #5a3a2a 40%, #a9a08a 75%, #3e3a2e 100%); }
  .add-to-cart { position: absolute; left: 0; bottom: 0; width: 240px; height: 42px; background: rgba(40, 40, 40, 0.92); color: #eee; font-size: 14px; line-height: 42px; }
  .product-name { margin-top: 10px; font-size: 15px; color: var(--ink-soft); }
  .product-price { margin-top: 4px; font-family: "Open Sans", Arial, sans-serif; font-size: 16px; font-weight: 700; color: var(--ink); }
  .product-price s { color: #888; font-weight: 600; margin-right: 2px; }
</style>
</head>
<body>

<header class="site-header">
  <div class="utility-left">
    <span class="flag-chip"></span><span class="caret"></span>
    <span style="margin-left:6px">$</span><span class="caret"></span>
    <span style="margin-left:6px">Call us on : 5550 118 42</span>
  </div>
  <div class="search">Search
    <svg width="14" height="14" viewBox="0 0 14 14"><circle cx="5.5" cy="5.5" r="4.3" fill="none" stroke="#9a9a9a" stroke-width="1.6"/><line x1="8.7" y1="8.7" x2="13" y2="13" stroke="#9a9a9a" stroke-width="1.8"/></svg>
  </div>

  <div class="brand">
    <div class="brand-dot"></div>
    <div class="brand-name">Coral Glow Luxe</div>
  </div>

  <div class="utility-right">
    <span>My Account</span><span class="caret"></span>
    <span style="margin-left:4px">:</span>
    <span>Wish List (0)</span>
  </div>
  <div class="cart">
    <svg width="14" height="17" viewBox="0 0 14 17"><rect x="1" y="5" width="12" height="11" fill="none" stroke="#9a9a9a" stroke-width="1.4"/><path d="M4 5V3.5a3 3 0 0 1 6 0V5" fill="none" stroke="#9a9a9a" stroke-width="1.4"/></svg>
    <span>( 0 items )</span><span class="caret"></span>
  </div>

  <nav class="main-nav">
    <a href="#">HOME</a>
    <a href="#">SHOP</a>
    <a href="#">ABOUT</a>
    <a href="#">CONTACT</a>
    <a href="#">STORE LOCATO</a>
    <a href="#" class="account-link"><b>SIGN IN</b> <span>OR</span> <b>CREATE AN ACCOUNT</b></a>
  </nav>
</header>

<div class="shipping-band"><strong>FREE SHIPPING</strong> ON ALL DOMESTIC ORDERS OVER $55. <u>CLICK FOR DETAILS</u></div>

<section class="hero">
  <div class="hero-photo" role="img" aria-label="Woman on a tropical beach wearing a gold metallic back tattoo, turquoise sea and overwater bungalows behind"></div>
  <div class="hero-panel"></div>
  <p class="hero-copy">Lorem ipsum dolor sit amet, consectetur adipisicing elit, sed do eiusmod tempor dolore magna aliqua.</p>
  <div class="hero-price">Only <strong>$35</strong></div>
  <div class="hero-kicker">LOOKS BRINGS</div>
  <div class="hero-title">happiness</div>
  <div class="hero-cta">SHOP NOW</div>
  <div class="hero-arrow prev"><svg width="10" height="16" viewBox="0 0 10 16"><path d="M8 1L2 8l6 7" fill="none" stroke="#bbb" stroke-width="1.6"/></svg></div>
  <div class="hero-arrow next"><svg width="10" height="16" viewBox="0 0 10 16"><path d="M2 1l6 7-6 7" fill="none" stroke="#ddd" stroke-width="1.6"/></svg></div>
  <div class="hero-dots"><span class="active"></span><span></span><span></span></div>
</section>

<div class="tabs">
  <span class="tab active">Bestseller</span>
  <span class="tab latest">Latest</span>
  <span class="tab special">Special</span>
  <span class="tab-underline"></span>
</div>
<svg class="tab-pointer" width="14" height="9" viewBox="0 0 14 9"><path d="M1 1l6 6 6-6" fill="none" stroke="#333" stroke-width="1.6"/></svg>
<div class="carousel-nav">
  <svg width="10" height="18" viewBox="0 0 10 18"><path d="M8 1L2 9l6 8" fill="none" stroke="#bbb" stroke-width="1.6"/></svg>
  <svg width="10" height="18" viewBox="0 0 10 18"><path d="M2 1l6 8-6 8" fill="none" stroke="#111" stroke-width="1.8"/></svg>
</div>

<section class="products">
  <article class="product">
    <div class="product-photo skin-a" role="img" aria-label="Woman's back with a gold jewelled spine tattoo">
      <div class="add-to-cart">Add to Cart</div>
    </div>
    <div class="product-name">Sable Reef Pro</div>
    <div class="product-price">$2,000.00</div>
  </article>
  <article class="product">
    <div class="product-photo skin-b" role="img" aria-label="Arms and hands decorated with ornate gold lace tattoos"></div>
    <div class="product-name">Aliquam Erat</div>
    <div class="product-price"><s>$122.00</s> $122.00</div>
  </article>
  <article class="product">
    <div class="product-photo skin-c" role="img" aria-label="Back view with a gold arrow spine tattoo and silver arm bands"></div>
    <div class="product-name">Arcu Vitae Imperdiet</div>
    <div class="product-price">$122.00</div>
  </article>
  <article class="product">
    <div class="product-photo skin-d" role="img" aria-label="Ankle wearing a gold and silver floral anklet tattoo"></div>
    <div class="product-name">Varius Neque At Enim</div>
    <div class="product-price">$1,202.00</div>
  </article>
</section>

</body>
</html>
```